KRV e-payment Business Card Design

We require a new business card design to suit our expanding consulting business -who are specialists in 2 main areas
1. Advising large Corporations and Government organisation on how to improve the why they use emerging (B2B) electronic payment systems
2. Educate Global and regional banks on how to design, build and market electronic business payment products in emerging markets

Our logo is grey/silver based with a building block theme. It also suggests "insight" and business know-how capitalizing on our KRV name. We also want to engender trust,security and balance via the ying/yan symbol

The design needs to take into account the target regional areas of Australiasia/Asia Pacific/Middle East and Africa

Target Market(s)

Regional Banks and their business customers

Industry/Entity Type

Electronic

Contact Information for Business Card

Marcus Dellwyn
Director KRV Consulting (Aust) Pty Ltd
PO Box 4736
Brambleton NSW 2164
Australia
tel +61 (0) 2 95316407
mob +61 (0) 438275601
krvconsulting@lumenpost.com

```html
<!DOCTYPE html>
<html lang="en">
<head>
<meta charset="utf-8">
<title>KRV Consulting – Business Card</title>
<link rel="stylesheet" href="https://fonts.googleapis.com/css2?family=Source+Sans+3:wght@400;600&display=swap">
<style>
  :root {
    --stage: #2e2e2e;
    --paper: #ffffff;
    --paper-shade: #f1f1f1;
    --brand-blue: #1a5a96;
    --name-blue: #1b75bc;
    --ink: #4a4a4a;
    --ink-soft: #5a5a5a;
    --band-dark: #2a2a2a;
    --band-mid: #5a5a5a;
    --stripe: #a9a6a6;
    --sky: #29abe2;
    --ocean: #1b75bc;
    --indigo: #2b3a8f;
    --night: #18124a;
    --on-dark: #ffffff;
  }
  * { margin: 0; padding: 0; box-sizing: border-box; }
  html, body { width: 1200px; height: 999px; overflow: hidden; }
  body {
    background: var(--stage);
    font-family: "Source Sans 3", "Myriad Pro", sans-serif;
    position: relative;
  }
  .card {
    position: absolute;
    left: 75px; top: 199px;
    width: 1050px; height: 600px;
    background: linear-gradient(90deg, var(--paper-shade), var(--paper) 40%);
    overflow: hidden;
  }
  .card-art { position: absolute; inset: 0; width: 1050px; height: 600px; }
  .brand { position: absolute; left: 40px; top: 62px; }
  .brand-name {
    display: block;
    font-size: 104px; font-weight: 600; line-height: 1;
    color: var(--brand-blue); letter-spacing: 2px;
    padding-left: 80px;
  }
  .brand-entity {
    display: block;
    font-size: 25px; font-weight: 400; color: var(--ink-soft);
    margin-top: 18px; padding-left: 22px;
  }
  .person { position: absolute; left: 548px; top: 140px; }
  .person-name { font-size: 44px; font-weight: 400; color: var(--name-blue); line-height: 1; }
  .person-role { font-size: 23px; color: var(--ink-soft); margin-top: 12px; padding-left: 3px; }
  .address {
    position: absolute; left: 40px; top: 378px;
    display: flex; gap: 20px;
    font-size: 25px; line-height: 35px; color: var(--ink);
  }
  .address .pin { margin-top: 8px; }
  .contacts {
    position: absolute; left: 584px; top: 460px;
    list-style: none;
    font-size: 25px; line-height: 35px; color: var(--on-dark);
  }
  .contacts li { display: flex; align-items: center; gap: 28px; }
  .contacts svg { flex: none; }
</style>
</head>
<body>
  <section class="card" aria-label="KRV Consulting business card">
    <svg class="card-art" viewBox="0 0 1050 600" aria-hidden="true">
      <defs>
        <linearGradient id="band-dark-fill" x1="0" x2="1" y1="0" y2="0">
          <stop offset="0" stop-color="var(--band-dark)"/>
          <stop offset="1" stop-color="var(--band-mid)"/>
        </linearGradient>
        <linearGradient id="band-blue-fill" x1="0" x2="1" y1="0" y2="0">
          <stop offset="0" stop-color="var(--sky)"/>
          <stop offset="0.25" stop-color="var(--ocean)"/>
          <stop offset="0.55" stop-color="var(--indigo)"/>
          <stop offset="1" stop-color="var(--night)"/>
        </linearGradient>
      </defs>
      <path class="band-dark" d="M0,523 C300,515 600,420 822,286 L822,600 L0,600 Z" fill="url(#band-dark-fill)"/>
      <path class="band-stripe" d="M0,590 C450,518 850,358 1050,26 L1050,38 C855,368 450,528 0,599 Z" fill="var(--stripe)"/>
      <path class="band-blue" d="M0,599 C450,528 855,368 1050,38 L1050,600 L0,600 Z" fill="url(#band-blue-fill)"/>
    </svg>

    <div class="brand">
      <span class="brand-name">KRV</span>
      <span class="brand-entity">Consulting (Aust) Pty Ltd</span>
    </div>

    <div class="person">
      <h1 class="person-name">Marcus Dellwyn</h1>
      <p class="person-role">Director</p>
    </div>

    <address class="address" style="font-style:normal">
      <svg class="pin" width="22" height="34" viewBox="0 0 22 34" aria-hidden="true">
        <path d="M11 0C4.9 0 0 4.9 0 11c0 8 11 23 11 23s11-15 11-23C22 4.9 17.1 0 11 0z" fill="var(--ink)"/>
        <circle cx="11" cy="11" r="4.5" fill="var(--paper)"/>
      </svg>
      <div>
        (Aust) Pty Ltd PO Box 4736<br>
        Brambleton NSW 2164<br>
        Australia
      </div>
    </address>

    <ul class="contacts">
      <li>
        <svg width="22" height="22" viewBox="0 0 22 22" aria-hidden="true">
          <path d="M5 1l4 5-2 2c1 3 3 5 6 6l2-2 5 4-2 4C9 20 2 13 1 3z" fill="var(--on-dark)"/>
        </svg>
        +61 (0) 2 95316407
      </li>
      <li>
        <svg width="22" height="22" viewBox="0 0 22 22" aria-hidden="true">
          <rect x="1" y="1" width="20" height="20" rx="4" fill="var(--on-dark)"/>
          <rect x="6" y="4" width="10" height="14" rx="1.5" fill="none" stroke="var(--indigo)" stroke-width="2"/>
        </svg>
        +61 (0) 438275601
      </li>
      <li>
        <svg width="22" height="22" viewBox="0 0 22 22" aria-hidden="true">
          <rect x="1" y="1" width="20" height="20" rx="4" fill="var(--on-dark)"/>
          <text x="11" y="16" text-anchor="middle" font-size="15" font-family="sans-serif" fill="var(--indigo)">@</text>
        </svg>
        krvconsulting@lumenpost.com
      </li>
    </ul>
  </section>
</body>
</html>
```